Brisket Vantle Orbis Holdings.com

We are doing a full website redesign. Here is a video explanation of what we need https://www.clipvessa.com/share/4b21f09a6ce347d1a85f2e7b90d15c66

THANK YOU SO MUCH!!

Here is a link to our current site
http://www.qentrifold.com

Target Market(s)

Pelwick QRX Sellers

Number of Pages Required

5+ page

Requirements
Must have
• Watch the video and follow the instructions!
• https://www.clipvessa.com/share/4b21f09a6ce347d1a85f2e7b90d15c66

```html
<!DOCTYPE html>
<html lang="en">
<head>
<meta charset="utf-8">
<title>Qentrifold.com – Login</title>
<link href="https://fonts.googleapis.com/css2?family=Raleway:wght@400;500&display=swap" rel="stylesheet">
<style>
  :root {
    --panel-bg: #1b1a1a;
    --text-main: #ffffff;
    --text-soft: #b9b9b9;
    --text-muted: #9a9a9a;
    --rule: #8d8d8d;
    --accent: #0a6aa6;
    --outline: #9c9c9c;
    --photo-dark: #2c2b29;
    --photo-mid: #5b5852;
    --photo-warm: #7a6248;
  }
  * { box-sizing: border-box; margin: 0; padding: 0; }
  html, body {
    width: 1200px; height: 625px; overflow: hidden;
    background: var(--panel-bg);
    font-family: "Raleway", sans-serif;
  }
  .screen { position: relative; width: 1200px; height: 625px; display: flex; }
  .login-panel {
    position: relative; width: 404px; height: 625px;
    background: var(--panel-bg); color: var(--text-main);
  }
  .brand-name {
    position: absolute; top: 119px; left: 0; width: 420px;
    text-align: center; font-size: 21px; font-weight: 400; letter-spacing: 0.2px;
  }
  .field {
    position: absolute; left: 87px; width: 241px;
    border-bottom: 1px solid var(--rule);
  }
  .field-username { top: 195px; height: 39px; }
  .field-password { top: 260px; height: 27px; }
  .field-label { display: block; font-size: 9px; color: var(--text-soft); }
  .field-value { display: block; margin-top: 5px; font-size: 12px; color: var(--text-main); }
  .field-placeholder { display: block; font-size: 12px; color: var(--text-muted); }
  .field-icon { position: absolute; right: 1px; top: 2px; }
  .btn-login {
    position: absolute; left: 87px; top: 325px; width: 241px; height: 40px;
    border-radius: 20px; background: var(--accent); color: var(--text-main);
    font-family: inherit; font-size: 12px; font-weight: 500; border: none;
  }
  .social-connect {
    position: absolute; left: 0; top: 381px; width: 416px;
    display: flex; align-items: center; justify-content: center; gap: 7px;
    font-size: 10.5px; color: var(--text-soft);
  }
  .social-dot { width: 15px; height: 15px; border-radius: 50%; background: #c9c9c9; }
  .btn-register {
    position: absolute; left: 87px; top: 454px; width: 241px; height: 40px;
    border-radius: 20px; border: 1px solid var(--outline); background: transparent;
    color: var(--text-soft); font-family: inherit; font-size: 11.5px;
  }
  .hero-photo {
    flex: 1; height: 625px;
    background: linear-gradient(160deg, var(--photo-mid) 0%, var(--photo-dark) 45%, var(--photo-warm) 75%, var(--photo-dark) 100%);
  }
</style>
</head>
<body>
<div class="screen">
  <section class="login-panel">
    <h1 class="brand-name">Qentrifold.com</h1>

    <div class="field field-username">
      <span class="field-label">Username</span>
      <span class="field-value">Thomas</span>
    </div>

    <div class="field field-password">
      <span class="field-placeholder">Password</span>
      <svg class="field-icon" width="14" height="16" viewBox="0 0 14 16" aria-hidden="true">
        <path d="M3.5 7V4.8a3.5 3.5 0 0 1 7 0V7" fill="none" stroke="#9a9a9a" stroke-width="1.2"/>
        <rect x="1.5" y="7" width="11" height="8" rx="2" fill="none" stroke="#9a9a9a" stroke-width="1.2"/>
        <circle cx="7" cy="11" r="1.2" fill="#9a9a9a"/>
      </svg>
    </div>

    <button class="btn-login">Login</button>

    <div class="social-connect">
      <span class="social-dot"></span>
      <span>Connect with Meshbook</span>
    </div>

    <button class="btn-register">Dont have account yet? Register</button>
  </section>

  <div class="hero-photo" role="img" aria-label="Photo of a team meeting: a presenter at a whiteboard and colleagues at a table with laptops showing charts"></div>
</div>
</body>
</html>
```